Letter Head Design - Finance industry

Design a letterhead to match the logo. Needs to be clean, simple and crisp. I'm open to suggestions. Will be using the logo that was submitted last with the W crossed over

Target Market(s)

Small medium businesses and government department's

Industry/Entity Type

Industry

Font styles to use
Sans Serif

Colors
cadf82
bcd85c
acd036
9bcb3c
e9e9e9
aaaaaa
000000
7f7f7f
b7b7b7

Requirements
Must have
• Need to display: Logo, Business address, ABN number, ASIC register number, contact phone, website, company email. Details are as per below:

Suite 4B Level 17
Marlowe Crest Tower
9 Kestin Lane
Sydney NSW 2000
Landline Ph: 02 9417 3065
Ph: 1300 5914 37
Email: enquiries@corvalmoney.com.au
W: www.corvalmoney.com.au

On the footer, the details below need to be specified:
ABN: 48 703 591 236
ASIC Registration Number: 73 418806521

Should not have
• No imagery or design that is not in line with the logo

```html
<!DOCTYPE html>
<html lang="en">
<head>
<meta charset="utf-8">
<title>Corval Money Letterhead</title>
<link href="https://fonts.googleapis.com/css2?family=Arimo:wght@400;700&family=Open+Sans:wght@400;600&display=swap" rel="stylesheet">
<style>
  :root {
    --backdrop: #3a3a3a;
    --paper: #f6f8f7;
    --brand-green: #9bcb3c;
    --accent-grey: #7f7f7f;
    --ink: #000000;
    --footer-grey: #8a8a8a;
    --divider: #aaaaaa;
    --white: #ffffff;
  }
  * { margin: 0; padding: 0; box-sizing: border-box; }
  html, body {
    width: 999px; height: 1200px; overflow: hidden;
    background: var(--backdrop);
  }
  .letterhead {
    position: absolute; left: 111px; top: 53px;
    width: 776px; height: 1094px;
    background: var(--paper);
    overflow: hidden;
  }
  .header-band {
    position: absolute; left: 0; top: 0; width: 776px; height: 150px;
    background: var(--brand-green);
  }
  .header-rule {
    position: absolute; left: 0; top: 156px; width: 776px; height: 6px;
    background: var(--accent-grey);
  }
  .brand-name {
    position: absolute; left: 56px; top: 54px;
    font-family: "Arimo", Arial, sans-serif; font-weight: 700;
    font-size: 27px; color: var(--white); letter-spacing: -0.3px;
  }
  .letter-body {
    position: absolute; left: 45px; top: 249px; width: 681px;
    font-family: "Arimo", Arial, sans-serif; font-size: 14.1px;
    line-height: 18.7px; color: var(--ink); text-align: justify;
  }
  .letter-body p { margin-bottom: 18.7px; }
  .signature-area {
    position: absolute; left: 590px; top: 876px; width: 120px; height: 86px;
    background: linear-gradient(135deg, #eef0ef, #f4f6f5);
    border-radius: 4px;
  }
  .letter-footer {
    position: absolute; left: 0; top: 1012px; width: 776px; height: 80px;
    font-family: "Open Sans", Arial, sans-serif; font-size: 11.6px;
    line-height: 15.6px; color: var(--footer-grey);
  }
  .footer-address { position: absolute; left: 45px; top: 3px; font-style: normal; }
  .footer-divider {
    position: absolute; top: 0; width: 1.5px; height: 78px;
    background: var(--divider);
  }
  .footer-divider.first { left: 219px; }
  .footer-divider.second { left: 508px; }
  .footer-contact { position: absolute; left: 280px; top: 2px; list-style: none; }
  .footer-contact li { display: flex; align-items: center; height: 16.6px; }
  .footer-contact svg { width: 11px; height: 11px; margin-right: 8px; fill: var(--footer-grey); }
  .footer-registration { position: absolute; left: 533px; top: 33px; }
</style>
</head>
<body>
<main class="letterhead">
  <div class="header-band"></div>
  <div class="header-rule"></div>
  <div class="brand-name">Corval Money</div>

  <section class="letter-body">
    <p>Lorem ipsum dolor sit amet, consectetur adipiscing elit. Proin porta, turpis sed elementum semper, est enim viverra nulla, non sollicitudin lorem felis ac enim. Duis varius arcu sed ipsum sollicitudin, vitae consequat ligula rhoncus. Donec blandit quam quis dui lobortis consequat. Vivamus in tempor turpis, sed mollis lacus. Maecenas ac libero erat. Suspendisse elit lacus, bibendum et arcu nec, malesuada vulputate nunc. Nunc enim ex, placerat sit amet porta eu, consequat a risus.</p>
    <p>Lorem ipsum dolor sit amet, consectetur adipiscing elit. Vestibulum pharetra enim at rutrum imperdiet. Aliquam sollicitudin efficitur purus. Integer eros lacus, pellentesque sed ornare eget, imperdiet lacinia est. Sed egestas erat eget erat dictum, et mattis lorem bibendum. Quisque at tellus egestas, finibus augue vel, semper urna. Donec facilisis mi in dui imperdiet, vel aliquet eros hendrerit. Nulla facilisi.</p>
    <p>Nam ipsum purus, pellentesque ac placerat quis, rhoncus quis nisl. Vivamus gravida placerat magna, quis vestibulum odio tincidunt quis. Fusce vitae tristique ipsum. Nam sed velit accumsan quam elementum venenatis. Sed non neque eget felis vulputate condimentum. Nunc ultrices in metus a congue. Maecenas ut erat eget orci feugiat pulvinar quis vitae libero. Sed finibus risus pellentesque libero malesuada hendrerit. Cum sociis natoque penatibus et magnis dis parturient montes, nascetur ridiculus mus. Vestibulum malesuada purus urna, pretium bibendum est iaculis id. Nullam dui arcu, gravida at felis eu, varius venenatis nunc. Sed rutrum pellentesque erat, finibus feugiat nunc porta ac.</p>
    <p>Morbi fringilla malesuada arcu, viverra congue mauris pellentesque sed. Duis elementum faucibus nulla, sit amet sodales lectus scelerisque sed. Pellentesque egestas lorem nulla, vel facilisis urna ultrices ac. Pellentesque ac felis in orci porttitor viverra. Integer tortor nunc, pulvinar id neque nec, convallis rutrum sem. Mauris sed velit erat. Nunc tincidunt, dui ut aliquet consequat, lorem justo accumsan nisi, eget mollis nisl erat non ante. Proin luctus mollis nibh, sit amet placerat mi tempus vel.</p>
    <p>Suspendisse finibus urna sed maximus mollis. Maecenas sit amet suscipit sapien. Donec a justo quis felis pellentesque sodales condimentum non risus. Ut dignissim pellentesque augue, id pharetra odio vulputate eget. Nam non porttitor sapien. Proin iaculis nisi a neque ultrices porta. Curabitur eu congue quam. Lorem ipsum dolor sit amet, consectetur adipiscing elit. Curabitur accumsan at augue ac vestibulum. Sed sed mattis velit. Proin eros risus, viverra nec urna ac, convallis fringilla massa. Pellentesque elementum ligula a sem sollicitudin mattis. Suspendisse eget pretium felis.</p>
  </section>

  <div class="signature-area" role="img" aria-label="Handwritten signature of the sender"></div>

  <footer class="letter-footer">
    <address class="footer-address">
      Suite 4B Level 17<br>
      Marlowe Crest Tower<br>
      9 Kestin Lane<br>
      Sydney NSW 2000
    </address>
    <span class="footer-divider first"></span>
    <ul class="footer-contact">
      <li><svg viewBox="0 0 12 12"><path d="M2.5,1 L4.5,1 L5.2,3.5 L4,4.5 C4.6,6 6,7.4 7.5,8 L8.5,6.8 L11,7.5 L11,9.5 C11,10.3 10.3,11 9.5,11 C5,11 1,7 1,2.5 C1,1.7 1.7,1 2.5,1 Z"/></svg>02 9417 3065</li>
      <li><svg viewBox="0 0 12 12"><path d="M2,1 H10 V11 H2 Z M3.5,2.5 V9.5 H8.5 V2.5 Z M5,8 H7 V9 H5 Z"/></svg>1300 5914 37</li>
      <li><svg viewBox="0 0 12 12"><path d="M1,2 H11 V10 H1 Z M2,3.2 V9 H10 V3.2 L6,6.3 Z M2.6,3 L6,5.5 L9.4,3 Z"/></svg>enquiries@corvalmoney.com.au</li>
      <li><svg viewBox="0 0 12 12"><path d="M6,1 A5,5 0 1 0 6.01,1 Z M6,2 A4,4 0 1 1 5.99,2 Z M1.5,5.5 H10.5 V6.5 H1.5 Z M5.5,1.5 H6.5 V10.5 H5.5 Z"/></svg>www.corvalmoney.com.au</li>
    </ul>
    <span class="footer-divider second"></span>
    <div class="footer-registration">
      ABN: 48 703 591 236<br>
      ASIC: Registration Number: XXXXXX
    </div>
  </footer>
</main>
</body>
</html>
```